Eye-catching Yellow Page Ad for Attorney's Office

We need a phone book advertisement for our law office. We practice workers' compensation law, and our clientele consists exclusively of individuals who have been injured on the job. The dimensions of the print ad will be 6" W X 4.54" H.

We've had our current ad for several years, and wanted to get a new one that has been designed by a professional. Being that it's an ad for a law firm, it needs to be professional looking, but we're hoping to have something that looks a little more modern and has eye-catching appeal. We like the text that is included in the ad, and we want to make sure our phone number is very visible. No real preference for color scheme.

I've attached a copy of our current ad. All the information included in there is accurate. Our office name is Thornbury & Lisle, PLLC. The ethical rules for attorney advertising require the PLLC to be included in the ad, but it can be smaller than the other text (see our current ad).

Target Market(s)

Our potential clients are injured workers looking for legal representation in their workers' compensation claim.

Industry/Entity Type

Attorney

Font styles to use
Serif
Sans Serif

Requirements
Must have
• Professional, but stands out from the crowd
Nice to have
• Clean modern design
Should not have
• We don't want it to be too crowded or over-worked.

```html
<!DOCTYPE html>
<html lang="en">
<head>
<meta charset="utf-8">
<title>Thornbury &amp; Lisle, PLLC</title>
<link rel="stylesheet" href="https://fonts.googleapis.com/css2?family=Oswald:wght@600;700&family=Roboto+Condensed:wght@400;700&display=swap">
<style>
  :root {
    --ink: #000000;
    --gold: #ffcc00;
    --paper: #ffffff;
    --photo-dark: #3a2a1c;
    --photo-warm: #a07a4a;
  }
  * { margin: 0; padding: 0; box-sizing: border-box; }
  html, body { width: 1200px; height: 907px; overflow: hidden; background: var(--paper); }
  .ad {
    position: relative; width: 1200px; height: 907px; overflow: hidden;
    background: var(--gold);
    font-family: "Roboto Condensed", "Arial Narrow", sans-serif;
  }
  .header-band { position: absolute; left: 0; top: 0; width: 1200px; height: 303px; background: var(--ink); }
  .firm-name {
    position: absolute; left: 44px; top: 10px; width: 1112px;
    color: var(--gold); font-weight: 700; font-size: 150px; line-height: 1;
    letter-spacing: 1px; white-space: nowrap;
  }
  .firm-suffix {
    position: absolute; right: 46px; top: 160px;
    color: var(--gold); font-size: 32px; line-height: 1;
  }
  .tagline {
    position: absolute; left: 47px; top: 188px;
    color: var(--gold); font-size: 24px; word-spacing: 8px; letter-spacing: 0.3px;
  }
  .promise {
    position: absolute; left: 47px; top: 218px;
    color: var(--paper); font-size: 24px; line-height: 28px;
  }
  .headline {
    position: absolute; left: 0; top: 0; width: 240px; height: 907px;
    font-family: "Oswald", "Arial Narrow", sans-serif; font-weight: 700;
    text-transform: uppercase;
  }
  .headline span {
    position: absolute; left: 44px; display: block;
    font-size: 88px; line-height: 1; white-space: nowrap;
  }
  .headline .word-we { top: 313px; font-size: 118px; letter-spacing: 4px; }
  .headline .word-can { top: 418px; }
  .headline .word-help { top: 496px; }
  .headline .word-you { top: 570px; }
  .headline .light { color: var(--paper); }
  .headline .dark { color: var(--ink); }
  .services { position: absolute; left: 247px; top: 312px; list-style: none; }
  .services li {
    position: relative; padding-left: 45px; height: 51.3px;
    font-weight: 700; font-size: 29px; line-height: 42px; color: var(--ink);
  }
  .services li::before {
    content: ""; position: absolute; left: 0; top: 11px;
    width: 24px; height: 22px; background: var(--ink);
  }
  .partners-photo {
    position: absolute; left: 734px; top: 224px; width: 424px; height: 388px;
    border: 4px solid var(--paper);
    background: linear-gradient(135deg, var(--photo-warm), var(--photo-dark) 55%, #7a5a36);
  }
  .partner-names {
    position: absolute; left: 736px; top: 630px;
    font-weight: 700; font-size: 31px; color: var(--ink);
  }
  .phone-icon { position: absolute; left: 38px; top: 694px; }
  .phone-number {
    position: absolute; left: 170px; top: 668px;
    font-weight: 700; font-size: 176px; line-height: 1; color: var(--ink); letter-spacing: -1px;
  }
  .footer-band {
    position: absolute; left: 0; top: 843px; width: 1200px; height: 64px; background: var(--ink);
    display: flex; justify-content: space-between; align-items: center; padding: 0 42px 0 44px;
    font-size: 31px; color: var(--paper);
  }
  .footer-band .label { color: var(--gold); }
</style>
</head>
<body>
<div class="ad">
  <div class="header-band"></div>
  <h1 class="firm-name">Thornbury &amp; Lisle</h1>
  <div class="firm-suffix">PLLC</div>
  <p class="tagline">Former Assistant Attorneys General Who Know The System</p>
  <p class="promise">At Thornbury &amp; Lisle, We provide personal attention to our clients,<br>That means your case is handled by an attorney not an assistant.</p>

  <div class="headline">
    <span class="word-we light">We</span>
    <span class="word-can dark">Can</span>
    <span class="word-help light">Help</span>
    <span class="word-you dark">You</span>
  </div>

  <ul class="services">
    <li>Workplaces Injuries or Death</li>
    <li>Lost Wages</li>
    <li>Medical Expenses &amp; Treatment</li>
    <li>Hearing Loss Claims</li>
    <li>Pension Claims</li>
    <li>Disability Awards</li>
    <li>Return to Work Issues</li>
  </ul>

  <div class="partners-photo" role="img" aria-label="Photo of the two partner attorneys standing in a law library, one holding an open book"></div>
  <div class="partner-names">Adrian Thornbury &amp; Claire Lisle</div>

  <svg class="phone-icon" width="122" height="122" viewBox="0 0 122 122" aria-hidden="true">
    <circle cx="61" cy="61" r="54" fill="none" stroke="var(--ink)" stroke-width="11"/>
    <path d="M38 34 l12 -4 l9 18 l-8 6 c4 9 10 15 19 19 l6 -8 l18 9 l-4 12 c-2 4 -7 5 -11 4 c-23 -6 -40 -23 -46 -46 c-1 -4 1 -9 5 -10 z" fill="var(--ink)"/>
  </svg>
  <div class="phone-number">360-555-0147</div>

  <div class="footer-band">
    <span><span class="label">reach:</span> 482 W. Harbor Suite 310, Fairhaven</span>
    <span><span class="label">website:</span> www.thornburylisle.com</span>
  </div>
</div>
</body>
</html>
```